Announcement for a New Trauma Therapy Group - Rack Card

I need a two-sided "rack" card that is 4x9 announcing a Women's Trauma and Loss Group. I am a licensed therapist and will be starting this support group for women who have experienced trauma of all kinds. In addition to groups, I offer individual, couples, and family counseling sessions.

I would like to see designs that are soft tones and use colors like muted blues, greens, and sand tones. The final design should communicate hope and healing as well as have a peaceful feel to it.

I would like a picture of a woman's profile from either the side or from behind her. (possibly a contemplative picture on a beach)

I am attaching a picture of myself to go alongside the bio information as well.

On One Side, I need the description of the group and contact info:

Mending the Weary Spirit
Women's Trauma & Loss Group
Led by Licensed Professional Counselor, Jen Dalby Rusk

10 Week Group
Cost - $35 session
Group size limited to 10 participants

Topics Include:
What is Trauma?
How Trauma Affects Us
Creating a Feeling of Safety
Managing Trauma Triggers
Importance of Self Care
Healthy vs. Unhealthy Coping
Guilt, Shame, and Blame
Victim vs. Victimized
Grieving through Loss
Anger and Forgiveness
Imagining a Better Future

For More Information, Contact:
Jen Dalby Rusk, LPC, LMFT
(555) 614-3920
jen@brightmeadowcare.example

On Side Two:

Life hurts and does not seem fair. So what do you do when you are faced with an event in your life that knocks you off your feet? It seems no one understands what you are feeling and no one knows just what to say. It is tempting to pull away and isolate or put up a mask and pretend everything is OK.

It is my desire you know that you are not alone! There are others who understand the feelings you are going through and offer a safe place for encouraging support. I want to invite you to embark on a courageous journey of healing where you will not only learn how to "survive" after trauma and loss, but instead, learn that you can once again "thrive"!
- Jen Dalby Rusk, LPC, LMFT

Jen Dalby Rusk is a Licensed Professional Counselor and Licensed Marriage and Family Therapist. She is the owner of Quiet Harbor Counseling Services located in Tulsa, OK.

Jen is a trauma survivor herself and understands firsthand the unique challenges that can arise on the journey to healing.

(Include Jen's picture next to bio)

(Attach logo and business information to this side as well.)

Target Market(s)

Women who have gone through a traumatic experience or loss and are hurting emotionally

Industry/Entity Type

Counsellor

Font styles to use
Serif
Script

Colors
fbe7d2
86cfc6
cfeae6
85abd2
cfdeed

Requirements
Must have
• Jen's picture as well as her logo and contact information must be on the card.
• One side of the card should describe the group with the following description:
• "Mending the Weary Spirit"
• Women's Trauma & Loss Group
• Led by Licensed Professional Counselor, Jen Dalby Rusk
• 10 Week Group
• Cost - $35 session
• Group size limited to 10 participants
• Topics Include:
• What is Trauma?
• How Trauma Affects Us
• Creating a Feeling of Safety
• Managing Trauma Triggers
• Importance of Self Care
• Healthy vs. Unhealthy Coping
• Guilt, Shame, and Blame
• Victim vs. Victimized
• Grieving through Loss
• Anger and Forgiveness
• Imagining a Better Future
• For More Information, Contact:
• Jen Dalby Rusk, LPC, LMFT
• (555) 614-3920
• jen@brightmeadowcare.example
• On the second side, it must have this note from Jen:
• Life hurts and does not seem fair. So what do you do when you are faced with an event in your life that knocks you off your feet? It seems no one understands what you are feeling and no one knows just what to say. It is tempting to pull away and isolate or put up a mask and pretend everything is OK.
• It is my desire you know that you are not alone! There are others who understand the feelings you are going through and offer a safe place for encouraging support. I want to invite you to embark on a courageous journey of healing where you will not only learn how to "survive" after trauma and loss, but instead, learn that you can once again "thrive"!
• - Jen Dalby Rusk, LPC, LMFT
• Jen Dalby Rusk is a Licensed Professional Counselor and Licensed Marriage and Family Therapist. She is the owner of Quiet Harbor Counseling Services located in Tulsa, OK.
• Jen is a trauma survivor herself and understands firsthand the unique challenges that can arise on the journey to healing. In addition to facilitating groups, Jen also offers individual, marriage, and family counseling.
Nice to have
• soft muted colors that are peaceful. Light blues, greens, sand colors would work well. A picture at the top of the card of either a woman or a woman's profile that is hopeful such as a woman sitting at a beach overlooking the ocean.
Should not have
• No harsh or bright bold colors. This card needs to have a peaceful feeling to it.

```html
<!DOCTYPE html>
<html lang="en">
<head>
<meta charset="utf-8">
<title>Mending the Weary Spirit – Rack Card</title>
<link rel="stylesheet" href="https://fonts.googleapis.com/css2?family=Lato:ital,wght@0,300;0,400;0,700;1,400;1,700&family=Playball&display=swap">
<style>
  :root{
    --page:#ecebe7;
    --white:#ffffff;
    --blue:#5fb6d6;
    --blue-deep:#3d9cc5;
    --blue-pale:#cfe6ee;
    --peach:#f7c6a2;
    --green:#6aa94f;
    --ink:#3b3b3b;
    --ink-soft:#5a5a5a;
    --sand:#efe3d4;
    --sky:#dfe9ef;
    --sea:#a7c8d3;
  }
  *{box-sizing:border-box;margin:0;padding:0}
  html,body{width:1200px;height:902px;overflow:hidden}
  body{background:var(--page);font-family:"Lato",sans-serif;color:var(--ink);position:relative}

  .rack-card{position:absolute;top:50px;width:356px;height:800px;background:var(--white);overflow:hidden}
  .rack-card--front{left:178px}
  .rack-card--back{left:598px}
  .layer{position:absolute;left:0;width:100%}

  /* front */
  .hero-art{top:0;height:290px}
  .room-backdrop{top:395px;height:350px;background:linear-gradient(180deg,rgba(255,255,255,1) 0%,rgba(239,227,212,.85) 12%,var(--sand) 55%,#e9dccb 100%)}
  .headline{top:254px;font-family:"Playball",cursive;line-height:1}
  .headline__top{display:block;font-size:58px;color:#3f3f3f;padding-left:26px}
  .headline__bottom{display:block;font-size:48px;color:var(--green);padding-left:98px;margin-top:-6px}
  .group-intro{top:404px;text-align:center}
  .group-intro__title{font-size:19px;font-weight:400;color:#4a4a4a}
  .group-intro__lead{font-size:12px;color:#555;margin-top:2px}
  .group-intro__weeks{font-size:20px;font-weight:700;color:var(--green);margin-top:9px;letter-spacing:.3px}
  .group-intro__detail{font-size:13px;color:#3a3a3a;line-height:16px}

  .topics{top:532px;left:33px;width:290px;height:118px;background:rgba(160,205,222,.55);border-radius:10px;padding:22px 14px 0 14px;display:grid;grid-template-columns:1fr 1fr;column-gap:6px}
  .topics__tab{position:absolute;top:-10px;left:50%;transform:translateX(-50%);background:var(--white);border:1.5px solid #8ccbd9;border-radius:12px;padding:2px 12px;font-size:11.5px;font-weight:700;color:#4b4b4b;white-space:nowrap}
  .topics__list{list-style:none}
  .topics__item{display:flex;align-items:center;gap:5px;font-size:8.4px;font-style:italic;color:#3f4a50;height:15px;white-space:nowrap}
  .topics__item svg{width:9px;height:9px;flex:none}

  .brand{display:flex;align-items:center;gap:8px}
  .brand__mark{width:14px;height:14px;border-radius:50%;background:var(--green);flex:none}
  .brand__name{font-size:15px;font-weight:400;color:var(--green);line-height:1.1}
  .brand--front{position:absolute;top:690px;left:0;width:100%;justify-content:center}

  .footer-band{bottom:0;height:62px}
  .contact-front{bottom:4px;text-align:center;color:var(--white);font-size:10px;line-height:12.5px}
  .contact-front__label{font-weight:700;color:#fbe7d2}
  .contact-front__name{font-weight:700}
  .contact-front svg{width:9px;height:9px;vertical-align:-1px;margin-right:3px}

  /* back */
  .letter-backdrop{top:0;height:250px;background:linear-gradient(160deg,#f4f6f7 0%,#e7ecef 45%,#dfe6ea 100%)}
  .letter{top:10px;padding:0 22px 0 60px;font-size:9.9px;font-style:italic;line-height:14.2px;color:#333}
  .letter p+p{margin-top:12px}
  .letter__sign{font-style:normal;font-weight:700;font-size:11.5px;margin-top:9px}
  .portrait-art{top:226px;height:320px}
  .bio{top:557px;padding:0 28px;font-size:10.6px;font-weight:700;line-height:13.6px;color:#454545}
  .bio p+p{margin-top:12px}
  .contact-back{top:644px;height:96px;display:flex;align-items:center}
  .contact-back .brand{width:155px;justify-content:center}
  .contact-back__rule{width:1px;height:96px;background:#bcd9e2}
  .contact-back__info{padding-left:18px}
  .contact-back__name{font-size:15px;font-weight:300;color:#444;letter-spacing:.3px}
  .contact-back__creds{list-style:none;margin-top:3px}
  .contact-back__creds li,.contact-back__reach li{display:flex;align-items:center;gap:6px}
  .contact-back__creds li{font-size:7.2px;color:var(--green);line-height:11px}
  .contact-back__reach{list-style:none;margin-top:14px}
  .contact-back__reach li{font-size:9.5px;color:#555;line-height:12.5px}
  .dot{width:3px;height:3px;border-radius:50%;background:#9cc9d6;flex:none}
  .footer-band--back{height:56px}
  .contact-footer{bottom:6px;text-align:center;color:var(--white);font-size:10.2px;font-weight:700;line-height:16px}
  .contact-footer svg{width:9px;height:9px;vertical-align:-1px;margin-right:4px}
</style>
</head>
<body>
<svg width="0" height="0" style="position:absolute" aria-hidden="true">
  <defs>
    <symbol id="tick" viewBox="0 0 10 10"><circle cx="5" cy="5" r="4.2" fill="none" stroke="#3f4a50" stroke-width="1"/><path d="M3 5.2l1.5 1.5L7.4 3.4" fill="none" stroke="#3f4a50" stroke-width="1.2"/></symbol>
    <symbol id="phone" viewBox="0 0 10 10"><circle cx="5" cy="5" r="4.4" fill="none" stroke="currentColor" stroke-width="1"/><path d="M3.4 2.8l1 .9-.5.8c.4.8.9 1.3 1.6 1.6l.8-.5.9 1-.7.8c-1.8-.3-3.2-1.7-3.6-3.6z" fill="currentColor"/></symbol>
    <symbol id="mail" viewBox="0 0 10 10"><rect x="1" y="2.5" width="8" height="5.5" fill="currentColor"/><path d="M1 2.5l4 3 4-3" fill="none" stroke="#3d9cc5" stroke-width=".8"/></symbol>
    <symbol id="globe" viewBox="0 0 10 10"><circle cx="5" cy="5" r="4.2" fill="none" stroke="currentColor" stroke-width="1"/><ellipse cx="5" cy="5" rx="1.8" ry="4.2" fill="none" stroke="currentColor" stroke-width=".8"/><path d="M1 5h8" stroke="currentColor" stroke-width=".8"/></symbol>
    <symbol id="pin" viewBox="0 0 10 10"><path d="M5 .8a3 3 0 0 1 3 3c0 2.2-3 5.6-3 5.6S2 6 2 3.8a3 3 0 0 1 3-3z" fill="currentColor"/><circle cx="5" cy="3.8" r="1.1" fill="#3d9cc5"/></symbol>
    <linearGradient id="blueSweep" x1="0" y1="0" x2="1" y2="1"><stop offset="0" stop-color="#9fd6e8"/><stop offset="1" stop-color="#3d9cc5"/></linearGradient>
    <linearGradient id="beachScene" x1="0" y1="0" x2="0" y2="1"><stop offset="0" stop-color="#e2ebef"/><stop offset=".45" stop-color="#a9c9d3"/><stop offset=".62" stop-color="#c9d8da"/><stop offset=".75" stop-color="#e6dccd"/><stop offset="1" stop-color="#dccfbd"/></linearGradient>
    <linearGradient id="duskScene" x1="0" y1="0" x2="0" y2="1"><stop offset="0" stop-color="#d9dfe6"/><stop offset=".3" stop-color="#b3aba0"/><stop offset=".55" stop-color="#a69a8a"/><stop offset="1" stop-color="#7f7a73"/></linearGradient>
  </defs>
</svg>

<!-- FRONT SIDE -->
<article class="rack-card rack-card--front">
  <svg class="layer hero-art" viewBox="0 0 356 290" width="356" height="290">
    <path d="M0 0H356V34C240 20 110 46 0 118Z" fill="url(#blueSweep)"/>
    <path d="M0 126C110 60 240 32 356 42" fill="none" stroke="var(--peach)" stroke-width="6"/>
    <path role="img" aria-label="Photo: a woman in a grey hooded top sitting on the sand, seen from behind, looking out at the sea" d="M0 138C110 72 240 50 356 52V196C290 246 190 264 60 258C30 256 10 252 0 248Z" fill="url(#beachScene)"/>
    <path d="M356 176C318 246 214 276 70 272C170 290 300 284 356 250Z" fill="url(#blueSweep)"/>
    <path d="M356 214C310 262 200 284 40 282C180 294 310 290 356 270Z" fill="var(--peach)" opacity=".9"/>
  </svg>

  <h1 class="layer headline"><span class="headline__top">Mending the</span><span class="headline__bottom">weary spirit</span></h1>

  <div class="layer room-backdrop" role="img" aria-label="Softly faded photo of a calm, warm-toned counseling room"></div>

  <section class="layer group-intro">
    <h2 class="group-intro__title">Women's Trauma &amp; Loss Group</h2>
    <p class="group-intro__lead">Led by Licensed Professional Counselor, Jen Dalby Rusk</p>
    <p class="group-intro__weeks">10 WEEK GROUP</p>
    <p class="group-intro__detail">Cost - $35 session</p>
    <p class="group-intro__detail">Group size limited to 10 participants</p>
  </section>

  <section class="layer topics">
    <h3 class="topics__tab">TOPICS INCLUDE:</h3>
    <ul class="topics__list">
      <li class="topics__item"><svg><use href="#tick"/></svg>What is Trauma?</li>
      <li class="topics__item"><svg><use href="#tick"/></svg>How Trauma Affects Us</li>
      <li class="topics__item"><svg><use href="#tick"/></svg>Creating a Feeling of Safety</li>
      <li class="topics__item"><svg><use href="#tick"/></svg>Managing Trauma Triggers</li>
      <li class="topics__item"><svg><use href="#tick"/></svg>Importance of Self Care</li>
      <li class="topics__item"><svg><use href="#tick"/></svg>Healthy vs. Unhealthy Coping</li>
    </ul>
    <ul class="topics__list">
      <li class="topics__item"><svg><use href="#tick"/></svg>Guilt, Shame, and Blame</li>
      <li class="topics__item"><svg><use href="#tick"/></svg>Victim vs. Victimized</li>
      <li class="topics__item"><svg><use href="#tick"/></svg>Grieving through Loss</li>
      <li class="topics__item"><svg><use href="#tick"/></svg>Anger and Forgiveness</li>
      <li class="topics__item"><svg><use href="#tick"/></svg>Imagining a Better Future</li>
    </ul>
  </section>

  <div class="brand brand--front">
    <span class="brand__mark"></span>
    <span class="brand__name">Quiet Harbor Counseling</span>
  </div>

  <svg class="layer footer-band" viewBox="0 0 356 62" width="356" height="62" preserveAspectRatio="none" aria-hidden="true">
    <path d="M0 10C120 -4 240 -4 356 10V62H0Z" fill="var(--peach)"/>
    <path d="M0 18C120 4 240 4 356 18V62H0Z" fill="url(#blueSweep)"/>
  </svg>
  <address class="layer contact-front" style="font-style:normal">
    <p class="contact-front__label">For More Information, Contact:</p>
    <p class="contact-front__name">Jen Dalby Rusk, LPC, LMFT</p>
    <p><svg><use href="#phone"/></svg>(555) 614-3920</p>
    <p><svg><use href="#mail"/></svg>jen@brightmeadowcare.example</p>
  </address>
</article>

<!-- BACK SIDE -->
<article class="rack-card rack-card--back">
  <div class="layer letter-backdrop" role="img" aria-label="Faded photo of a woman in a white dress standing by the sea with mountains beyond"></div>

  <section class="layer letter">
    <p>Life hurts and does not seem fair. So what do you do when you are faced with an event in your life that knocks you off your feet? It seems no one understands what you are feeling and no one knows just what to say. It is tempting to pull away and isolate or put up a mask and pretend everything is OK.</p>
    <p>It is my desire you know that you are not alone! There are others who understand the feelings you are going through and offer a safe place for encouraging support. I want to invite you to embark on a courageous journey of healing where you will not only learn how to "survive" after trauma and loss, but instead, learn that you can once again "thrive"!</p>
    <p class="letter__sign">- Jen Dalby Rusk, LPC, LMFT</p>
  </section>

  <svg class="layer portrait-art" viewBox="0 0 356 320" width="356" height="320">
    <path d="M0 60C120 10 260 4 356 44V20C260 -8 120 -2 0 40Z" fill="url(#blueSweep)"/>
    <path d="M0 64C120 18 260 12 356 50" fill="none" stroke="var(--peach)" stroke-width="6"/>
    <path role="img" aria-label="Photo of the counselor sitting on a rock on a beach at dusk, dunes and wooden stairs behind her" d="M0 70C120 26 250 20 356 58V262C260 308 100 306 0 262Z" fill="url(#duskScene)"/>
    <path d="M0 268C100 312 260 312 356 268" fill="none" stroke="var(--peach)" stroke-width="7"/>
    <path d="M0 280C100 326 260 326 356 280V296C260 336 100 336 0 296Z" fill="url(#blueSweep)"/>
  </svg>

  <section class="layer bio">
    <p>Jen Dalby Rusk is a Licensed Professional Counselor and Licensed Marriage and Family Therapist. She is the owner of Quiet Harbor Counseling Services located in Tulsa, OK.</p>
    <p>Jen is a trauma survivor herself and understands firsthand the unique challenges that can arise on the journey to healing.</p>
  </section>

  <section class="layer contact-back">
    <div class="brand">
      <span class="brand__mark"></span>
      <span class="brand__name">Quiet Harbor<br>Counseling</span>
    </div>
    <div class="contact-back__rule"></div>
    <div class="contact-back__info">
      <p class="contact-back__name">Jen Rusk, LPC-S, LMFT</p>
      <ul class="contact-back__creds">
        <li><span class="dot"></span>Licensed Professional Counselor</li>
        <li><span class="dot"></span>Licensed Marriage and Family Therapist</li>
      </ul>
      <ul class="contact-back__reach">
        <li><span class="dot"></span>555.614.3920</li>
        <li><span class="dot"></span>jen@brightmeadowcare.example</li>
      </ul>
    </div>
  </section>

  <svg class="layer footer-band footer-band--back" viewBox="0 0 356 56" width="356" height="56" preserveAspectRatio="none" aria-hidden="true">
    <path d="M0 2C60 20 296 20 356 2V56H0Z" fill="var(--peach)"/>
    <path d="M0 10C60 26 296 26 356 10V56H0Z" fill="url(#blueSweep)"/>
  </svg>
  <address class="layer contact-footer" style="font-style:normal">
    <p><svg><use href="#globe"/></svg>www.brightmeadowcare.example</p>
    <p><svg><use href="#pin"/></svg>4820 E. Harbor Lane #210 Tulsa, OK 74100</p>
  </address>
</article>
</body>
</html>
```